Autobody repair paint repairs spray painting bodywork crash repairs

Details for my new Facebook Design Project will be added sooAUTOMOTIVE REPAIR. CAR / MOTORCYCLES GOT LOGO DESIGN / DID THINK ABOUT FACEBOOK DONT NOALREADY HAVE WEB ADRESS www.brenvaro.co.uk and mail sales@brenvaro,co.uk NEED SOMETHINK I CAN MANAGE TO UPLOAD PICTURES IN TO A GALLERY OR SOMETHINGLIKE THAT I ALSO SELL CAR AND MOTORCYCLES MAYBE A SELLS PAGE WITH A QUIDLOOP LINKn.

Target Market(s)

general public and trade

Industry/Entity Type

Auto Repair

Font styles to use
Serif
Sans Serif

Colors

Designer to choose colors to be used in the design.

Requirements
Must have
• copy description from my website
• quidloop link. to my site shop
• plenty of logo within reason
Nice to have
• scolling shop
• easy to manage

```html
<!DOCTYPE html>
<html lang="en">
<head>
<meta charset="utf-8">
<title>Brenvaro Bodyshop – Facebook Cover</title>
<link rel="stylesheet" href="https://fonts.googleapis.com/css2?family=Oswald:wght@400;500;600&family=Montserrat:wght@500&display=swap">
<style>
  :root {
    --navy-deep: #0a1738;
    --navy-mid: #15295c;
    --navy-light: #23407f;
    --red: #e0242b;
    --white: #ffffff;
    --silver: #e4e7ec;
    --photo-dark: #2f3a33;
    --photo-mid: #5d6b5c;
    --photo-light: #9aa39a;
    --road: #3b3f44;
  }
  * { margin: 0; padding: 0; box-sizing: border-box; }
  html, body { width: 1200px; height: 458px; overflow: hidden; background: var(--white); }
  .cover {
    position: relative;
    width: 1200px;
    height: 458px;
    overflow: hidden;
    font-family: "Oswald", sans-serif;
    color: var(--white);
  }
  .hero-photo {
    position: absolute;
    inset: 0;
    background:
      radial-gradient(ellipse 260px 120px at 790px 300px, rgba(200,30,40,0.85), rgba(200,30,40,0) 100%),
      linear-gradient(170deg, var(--photo-light) 0%, var(--photo-mid) 35%, var(--photo-dark) 60%, var(--road) 100%);
  }
  .brand-panel {
    position: absolute;
    inset: 0;
    background: linear-gradient(160deg, var(--navy-light) 0%, var(--navy-mid) 40%, var(--navy-deep) 100%);
    clip-path: polygon(0 0, 680px 0, 495px 458px, 0 458px);
  }
  .brand {
    position: absolute;
    left: 34px;
    top: 40px;
    width: 700px;
  }
  .brand-name {
    display: flex;
    align-items: center;
    gap: 18px;
    font-family: "Oswald", sans-serif;
    font-weight: 500;
    font-size: 86px;
    line-height: 1;
    letter-spacing: 10px;
    color: var(--silver);
  }
  .brand-dot {
    width: 22px;
    height: 22px;
    border-radius: 50%;
    background: var(--red);
  }
  .brand-sub {
    margin-top: 16px;
    margin-left: 148px;
    font-family: "Montserrat", sans-serif;
    font-weight: 500;
    font-size: 32px;
    letter-spacing: 15px;
    color: var(--silver);
  }
  .tagline {
    position: absolute;
    left: 30px;
    top: 176px;
    font-weight: 500;
    font-size: 50px;
    line-height: 1;
    letter-spacing: 0.5px;
    text-transform: uppercase;
  }
  .tagline .accent { color: var(--red); }
  .services {
    position: absolute;
    left: 22px;
    top: 250px;
    list-style: none;
  }
  .services li {
    display: flex;
    align-items: center;
    gap: 12px;
    height: 36.6px;
    font-weight: 400;
    font-size: 21px;
    text-transform: uppercase;
    letter-spacing: 0.3px;
  }
  .tick { width: 24px; height: 24px; flex: none; }
  .address {
    position: absolute;
    right: 22px;
    top: 20px;
    text-align: right;
    font-weight: 500;
    font-size: 20px;
    line-height: 1.4;
    text-transform: uppercase;
  }
  .address .postcode { color: var(--red); }
  .contact {
    position: absolute;
    right: 22px;
    bottom: 22px;
    text-align: right;
    font-weight: 500;
    font-size: 21px;
    line-height: 1.95;
    text-transform: uppercase;
  }
</style>
</head>
<body>
<div class="cover">
  <div class="hero-photo" role="img" aria-label="Red sports coupe driving on a tree-lined country road"></div>
  <div class="brand-panel"></div>

  <div class="brand">
    <div class="brand-name">BRENVARO<span class="brand-dot"></span></div>
    <div class="brand-sub">BODYSHOP</div>
  </div>

  <h1 class="tagline">Your one stop <span class="accent">body</span> shop</h1>

  <ul class="services">
    <li><svg class="tick" viewBox="0 0 24 24"><path d="M3 13 L9 19 L21 4" fill="none" stroke="#e0242b" stroke-width="4" stroke-linecap="round" stroke-linejoin="round"/></svg>Full or part resprays</li>
    <li><svg class="tick" viewBox="0 0 24 24"><path d="M3 13 L9 19 L21 4" fill="none" stroke="#e0242b" stroke-width="4" stroke-linecap="round" stroke-linejoin="round"/></svg>Dent &amp; scratch removal</li>
    <li><svg class="tick" viewBox="0 0 24 24"><path d="M3 13 L9 19 L21 4" fill="none" stroke="#e0242b" stroke-width="4" stroke-linecap="round" stroke-linejoin="round"/></svg>Bumper repair</li>
    <li><svg class="tick" viewBox="0 0 24 24"><path d="M3 13 L9 19 L21 4" fill="none" stroke="#e0242b" stroke-width="4" stroke-linecap="round" stroke-linejoin="round"/></svg>Accident repair</li>
    <li><svg class="tick" viewBox="0 0 24 24"><path d="M3 13 L9 19 L21 4" fill="none" stroke="#e0242b" stroke-width="4" stroke-linecap="round" stroke-linejoin="round"/></svg>Alloy wheel's refurbished, repaired &amp; painted</li>
  </ul>

  <address class="address" style="font-style:normal">
    Hollin Trade Park,<br>
    Ferry Road, Ashbrook,<br>
    Northshire <span class="postcode">NX14 7QT</span>
  </address>

  <div class="contact">
    <div class="phone">07700900418</div>
    <div class="web">www.brenvaro.co.uk</div>
  </div>
</div>
</body>
</html>
```